Solar panel cleaning flyer design.

I'm looking for a flyer design for my new company called Brightfield Panel Works. We are a South Australian company that professionally clean residential and commercial solar panels. We generate leads by going door to door and need a flyer to hand out to our customers if they are interested in our service. As we are a new company we don't have anything particular in mind so be creative! Must include the company name and logo.

```html
<!DOCTYPE html>
<html lang="en">
<head>
<meta charset="UTF-8">
<title>Brightfield Panel Works – Flyer</title>
<link href="https://fonts.googleapis.com/css2?family=Arimo:wght@400;700&display=swap" rel="stylesheet">
<style>
  :root {
    --green: #7ab52f;
    --blue: #1d6db5;
    --blue-deep: #0d4d8c;
    --sky-top: #7fb6e4;
    --sky-light: #dcecf8;
    --panel: #24508e;
    --text: #4a4a4a;
    --white: #ffffff;
  }
  * { margin: 0; padding: 0; box-sizing: border-box; }
  html, body { width: 851px; height: 1200px; overflow: hidden; background: var(--white); }
  body { font-family: "Arimo", Arial, sans-serif; color: var(--text); }
  .flyer { position: relative; width: 851px; height: 1200px; overflow: hidden; background: var(--white); }

  .hero {
    position: absolute; left: 0; top: 0; width: 851px; height: 470px;
    background: linear-gradient(160deg, var(--sky-top) 0%, var(--sky-light) 30%, #5d8fc8 55%, var(--panel) 100%);
  }
  .hero-title {
    position: absolute; left: 34px; top: 26px; width: 780px;
    color: var(--white); font-weight: 700; font-size: 33px; line-height: 1.12;
    text-transform: uppercase;
  }
  .hero-wave { position: absolute; left: 0; top: 370px; width: 851px; height: 110px; }

  .intro { position: absolute; left: 34px; top: 520px; width: 440px; }
  .intro-title {
    color: var(--green); font-weight: 700; font-size: 27px; line-height: 1.15;
    text-transform: uppercase; margin-bottom: 20px; width: 460px;
  }
  .intro-body { font-size: 25px; line-height: 35.5px; color: var(--text); width: 410px; }

  .services {
    position: absolute; left: 505px; top: 482px; width: 314px; height: 398px;
    background: var(--green); border-radius: 0 0 36px 36px;
    color: var(--white); padding: 26px 22px 0 30px;
  }
  .services-title { font-size: 30px; font-weight: 400; text-align: center; text-transform: uppercase; margin-bottom: 14px; }
  .services-body { font-size: 25px; line-height: 1.22; }

  .brand {
    position: absolute; left: 505px; top: 905px; width: 314px;
    display: flex; flex-direction: column; align-items: center; gap: 14px;
  }
  .brand-dot { width: 70px; height: 70px; border-radius: 50%; background: var(--blue); }
  .brand-name { font-size: 30px; font-weight: 700; color: var(--blue); text-align: center; line-height: 1.1; }

  .footer {
    position: absolute; left: 0; top: 1082px; width: 851px; height: 118px;
    background: var(--green);
  }
  .footer-text {
    padding-top: 28px; text-align: center; color: var(--white);
    font-size: 31px; font-weight: 400; text-transform: uppercase; letter-spacing: 0.3px;
  }
</style>
</head>
<body>
<main class="flyer">
  <section class="hero" role="img" aria-label="Photo of rooftop solar panels under a bright blue sky"></section>
  <h1 class="hero-title">Lorem ipsum dolor sit amet, consectetur adipisicing elit, sed</h1>

  <svg class="hero-wave" viewBox="0 0 851 110" preserveAspectRatio="none" aria-hidden="true">
    <path d="M0 40 C 220 0, 520 80, 851 20 L851 110 L0 110 Z" fill="var(--blue-deep)"/>
    <path d="M0 52 C 220 15, 520 92, 851 34 L851 110 L0 110 Z" fill="var(--green)"/>
    <path d="M0 64 C 220 30, 520 104, 851 48 L851 110 L0 110 Z" fill="var(--white)"/>
  </svg>

  <section class="intro">
    <h2 class="intro-title">Lorem ipsum dolor sit amet, consectetur adipisicing</h2>
    <p class="intro-body">Lorem ipsum dolor sit amet, consectetur adipisicing elit, sed do eiusmod tempor incididunt ut labore et dolore magna aliqua. Ut enim ad minim veniam, quis nostrud exercitation ullamco laboris nisi ut aliquip ex ea commodo consequat. Duis aute irure dolor in reprehenderit in voluptate velit esse cillum dolore eu fugiat nulla pariatur. Excepteur sint occaecat cupidatat non</p>
  </section>

  <aside class="services">
    <h2 class="services-title">Our Services</h2>
    <p class="services-body">Lorem ipsum dolor sit amet, consectetur adipisicing elit, sed do eiusmod tempor incididunt ut labore et dolore magna aliqua. Ut enim ad minim veniam, quis nostrud</p>
  </aside>

  <div class="brand">
    <span class="brand-dot" aria-hidden="true"></span>
    <p class="brand-name">Brightfield Panel Works</p>
  </div>

  <footer class="footer">
    <p class="footer-text">For more information call</p>
  </footer>
</main>
</body>
</html>
```